Awesome photographers card for an awesome new business

Double sided business card Black background and silver logo in middle on one side. Details on otherside. please keep it simple

Industry/Entity Type

Photographer

Contact Information for Business Card

Colin Fairweather
0452816307
ColinFairweatherPhotography57@mailvane.com
www.ColinFairweatherPhotography.com.au
Instagram _Colin_fairweather

Requirements
Must have
• My logo in Silver
• please use instagram logo instead of "Instagram"

```html
<!DOCTYPE html>
<html lang="en">
<head>
<meta charset="utf-8">
<title>Colin Fairweather Photography – Business Card</title>
<link href="https://fonts.googleapis.com/css2?family=Roboto+Condensed:wght@700&family=Roboto:wght@400;500&display=swap" rel="stylesheet">
<style>
  :root {
    --backdrop: #2a2a2c;
    --card: #1c1c1d;
    --silver: #d6d6d8;
    --white: #f4f4f4;
    --icon-grey: #8e8e92;
    --divider: #6a6a6e;
  }
  * { box-sizing: border-box; margin: 0; padding: 0; }
  html, body {
    width: 1200px;
    height: 900px;
    overflow: hidden;
    background: var(--backdrop);
  }
  .sheet {
    width: 1200px;
    height: 900px;
    display: flex;
    flex-direction: column;
    align-items: center;
    justify-content: center;
    gap: 36px;
  }
  .card {
    width: 660px;
    height: 378px;
    background: var(--card);
    position: relative;
  }

  /* Front side */
  .card--front {
    display: flex;
    flex-direction: column;
    align-items: center;
    justify-content: center;
    gap: 38px;
  }
  .brand {
    display: flex;
    align-items: center;
    gap: 18px;
  }
  .brand__circle {
    width: 74px;
    height: 74px;
    border-radius: 50%;
    border: 3px solid var(--silver);
  }
  .brand__name {
    font-family: "Roboto", sans-serif;
    font-weight: 500;
    font-size: 30px;
    letter-spacing: 1px;
    color: var(--silver);
  }
  .front-url {
    font-family: "Roboto", sans-serif;
    font-weight: 500;
    font-size: 15px;
    letter-spacing: 3px;
    color: var(--white);
  }

  /* Back side */
  .card--back {
    display: flex;
    align-items: center;
  }
  .holder-name {
    width: 300px;
    padding-right: 22px;
    text-align: right;
    font-family: "Roboto Condensed", sans-serif;
    font-weight: 700;
    font-size: 28px;
    color: var(--silver);
    text-transform: uppercase;
  }
  .divider {
    width: 2px;
    height: 92px;
    background: var(--divider);
  }
  .contacts {
    list-style: none;
    padding-left: 18px;
    display: flex;
    flex-direction: column;
    gap: 4px;
  }
  .contacts__item {
    display: flex;
    align-items: center;
    gap: 9px;
    font-family: "Roboto", sans-serif;
    font-size: 13.5px;
    color: var(--white);
    line-height: 1.2;
  }
  .contacts__icon {
    width: 14px;
    height: 14px;
    flex: none;
    fill: var(--icon-grey);
  }
  .contacts__badge {
    width: 13px;
    height: 13px;
    flex: none;
    background: var(--icon-grey);
    border-radius: 2px;
  }
</style>
</head>
<body>
<main class="sheet">
  <section class="card card--front" aria-label="Card front">
    <div class="brand">
      <span class="brand__circle"></span>
      <span class="brand__name">Colin Fairweather</span>
    </div>
    <p class="front-url">www.ColinFairweatherPhotography.com.au</p>
  </section>

  <section class="card card--back" aria-label="Card back">
    <h1 class="holder-name">Colin Fairweather</h1>
    <span class="divider"></span>
    <ul class="contacts">
      <li class="contacts__item">
        <svg class="contacts__icon" viewBox="0 0 24 24" aria-hidden="true"><path d="M6.6 10.8a15.1 15.1 0 0 0 6.6 6.6l2.2-2.2a1 1 0 0 1 1-.25 11.4 11.4 0 0 0 3.6.57 1 1 0 0 1 1 1V20a1 1 0 0 1-1 1A17 17 0 0 1 3 4a1 1 0 0 1 1-1h3.5a1 1 0 0 1 1 1c0 1.25.2 2.45.57 3.57a1 1 0 0 1-.25 1z"/></svg>
        <span>0452816307</span>
      </li>
      <li class="contacts__item">
        <svg class="contacts__icon" viewBox="0 0 24 24" aria-hidden="true"><path d="M2 5h20v14H2z M4 7v.4l8 5.2 8-5.2V7z" fill-rule="evenodd"/></svg>
        <span>ColinFairweatherPhotography57@mailvane.com</span>
      </li>
      <li class="contacts__item">
        <svg class="contacts__icon" viewBox="0 0 24 24" aria-hidden="true"><circle cx="12" cy="12" r="10"/><path d="M2 12h20M12 2c3 3 3 17 0 20M12 2c-3 3-3 17 0 20" stroke="#1c1c1d" stroke-width="1.6" fill="none"/></svg>
        <span>www.ColinFairweatherPhotography.com.au</span>
      </li>
      <li class="contacts__item">
        <span class="contacts__badge"></span>
        <span>Colin_fairweather</span>
      </li>
    </ul>
  </section>
</main>
</body>
</html>
```